Tease by Dusk Age Verification Landing Page

To create a visually appealing design for the landing page of the adult game "Tease by Dusk" that confirms the visitor's age.
The design should have a simple and visually appealing look that focuses on two buttons labeled "Yes" and "No". The purpose of the page is to confirm that the visitor is 18 years of age or older before accessing the game's content. Responsive design that works well on desktop and mobile devices. The final output should be delivered in PSD, AI, or Sketch format, along with any necessary images or assets.
I have also attached examples.

```html
<!DOCTYPE html>
<html lang="en">
<head>
<meta charset="utf-8">
<title>Tease by Dusk – Age Verification</title>
<link href="https://fonts.googleapis.com/css2?family=Red+Hat+Display:wght@500;600;700&display=swap" rel="stylesheet">
<style>
  :root {
    --bg: #000000;
    --scene-deep: #2a0508;
    --scene-mid: #5a0c14;
    --panel: rgba(24, 24, 24, 0.94);
    --panel-line: rgba(255, 255, 255, 0.06);
    --accent: #d0105a;
    --accent-border: #b0102e;
    --text: #ffffff;
    --icon-bg: #141414;
  }
  * { box-sizing: border-box; margin: 0; padding: 0; }
  html, body {
    width: 1200px; height: 547px; overflow: hidden;
    background: var(--bg);
    font-family: "Red Hat Display", "Helvetica Neue", Arial, sans-serif;
    color: var(--text);
  }
  .stage { position: relative; width: 1200px; height: 547px; overflow: hidden; }
  .backdrop {
    position: absolute; inset: 0;
    background:
      radial-gradient(ellipse 180px 300px at 560px 300px, var(--scene-mid) 0%, transparent 75%),
      radial-gradient(ellipse 320px 360px at 540px 320px, var(--scene-deep) 0%, transparent 80%),
      var(--bg);
  }
  .music-toggle {
    position: absolute; left: 1060px; top: 19px;
    width: 41px; height: 41px;
    border: 1px solid var(--accent-border);
    background: var(--icon-bg);
    display: flex; align-items: center; justify-content: center;
  }
  .verify-frame {
    position: absolute; left: 370px; top: 185px;
    width: 442px; height: 270px;
    border: 1px solid var(--panel-line);
  }
  .verify-panel {
    position: absolute; left: 380px; top: 177px;
    width: 440px; height: 269px;
    background: var(--panel);
  }
  .brand {
    position: absolute; left: 0; right: 0; top: 103px;
    display: flex; flex-direction: column; align-items: center;
  }
  .brand-mark { width: 68px; height: 83px; background: var(--accent); }
  .brand-name {
    margin-top: 10px;
    font-size: 30px; font-weight: 700; letter-spacing: 0.2px;
    color: var(--text);
  }
  .question {
    position: absolute; left: 0; right: 0; top: 318px;
    text-align: center; font-size: 19.5px; font-weight: 600;
  }
  .choices {
    position: absolute; left: 541px; top: 358px;
    display: flex; gap: 10px;
  }
  .choice {
    width: 54px; height: 42px;
    background: var(--accent); color: var(--text);
    border: none; font: inherit; font-size: 17px; font-weight: 600;
    display: flex; align-items: center; justify-content: center;
  }
  .remember {
    position: absolute; left: 543px; top: 413px;
    display: flex; align-items: center; gap: 12px;
    font-size: 12.5px; font-weight: 500;
  }
  .remember-box { width: 8px; height: 8px; background: var(--text); }
</style>
</head>
<body>
  <main class="stage">
    <div class="backdrop" role="img" aria-label="Dimmed photograph of a dancer's legs in red light beside an illuminated pole"></div>

    <div class="music-toggle" aria-label="Toggle music">
      <svg width="22" height="22" viewBox="0 0 24 24" fill="#ffffff" aria-hidden="true">
        <path d="M8 4.5 L20 2 V16.5 A3 3 0 1 1 18 13.7 V6.2 L10 7.9 V18.5 A3 3 0 1 1 8 15.7 Z"/>
      </svg>
    </div>

    <div class="verify-frame"></div>
    <section class="verify-panel" aria-label="Age verification"></section>

    <div class="brand">
      <div class="brand-mark"></div>
      <div class="brand-name">Tease by Dusk</div>
    </div>

    <h1 class="question">Are You Over 18 years of Age?</h1>

    <div class="choices">
      <button class="choice choice-yes">Yes</button>
      <button class="choice choice-no">No</button>
    </div>

    <label class="remember">
      <span class="remember-box"></span>
      <span>Remember Me</span>
    </label>
  </main>
</body>
</html>
```